Chiropractic office needs updated web site

take the information/content from my existing website and redesign it to be more efficient and modern looking. i have a logo already designed that i have provided the files for. my office sees primarily athletes and their families and is geared toward active, healthy people who have sports injuries.
Updates

i originally started the project in february 2019 but am now just able to post the project. i need a new deadline calculated from todays (6-9-19) date.

Target Market(s)

injured athletes looking for a specific type of chiropractor.

Industry/Entity Type

Health Care

Contact Information for Business Card

I have a logo already designed and will provide that to all designers!

Coding

Coded - Design and coding required

Number of Pages Required

1 page

Font styles to use
Sans Serif

Colors

Designer to choose colors to be used in the design.

Requirements
Must have
• the current information/content already contained in my current website, belvanspinefit.com. i want this info redesigned and/or transferred to a new template. i will also provide new updated photos for use on the new site!
Nice to have
• modern, minimalist, creative looking website
Should not have
• typical medical website with boring, over-used stock photos of doctors, nurses and generic family types

```html
<!DOCTYPE html>
<html lang="en">
<head>
<meta charset="utf-8">
<title>Belvan Chiropractic and Sports Therapy</title>
<link rel="stylesheet" href="https://fonts.googleapis.com/css2?family=Poppins:wght@400;500;600;700&family=Lato:wght@400;700&display=swap">
<style>
:root{
  --red:#d7141f;
  --red-dark:#b5101a;
  --blue:#0e9acd;
  --blue-light:#0fb4ea;
  --ink:#111;
  --grey:#777;
  --grey-light:#999;
  --panel:#f4f4f4;
  --white:#fff;
}
*{box-sizing:border-box;margin:0;padding:0}
html,body{width:1200px;height:2406px;overflow:hidden}
body{font-family:"Lato",sans-serif;background:var(--white);color:var(--ink);position:relative}
.brand{display:flex;align-items:center;gap:10px}
.brand-dot{width:44px;height:44px;border-radius:50%;background:var(--blue)}
.brand-name{font-family:"Poppins",sans-serif;font-weight:600;font-size:20px;letter-spacing:3px;color:var(--blue);line-height:1.1}
.site-header{position:absolute;top:0;left:0;width:1200px;height:115px;display:flex;align-items:center;padding:0 77px}
.nav{display:flex;gap:28px;margin-left:auto;align-items:center;font-size:15px;color:var(--grey)}
.nav .active{color:var(--red);font-weight:700}
.hero{position:absolute;top:115px;left:0;width:1200px;height:625px;border-radius:0 0 50% 50% / 0 0 105px 105px;overflow:hidden;background:linear-gradient(100deg,#6d6f6c 0%,#8c8476 35%,#9a5a4e 55%,#a0635a 75%,#c4b8a4 100%)}
.hero-text{position:absolute;left:79px;top:105px;width:520px;color:var(--white)}
.hero h1{font-family:"Poppins",sans-serif;font-weight:700;font-size:45px;line-height:52px;letter-spacing:1px;text-shadow:0 2px 4px rgba(0,0,0,.35)}
.hero p{font-size:17px;line-height:31px;margin-top:18px}
.btn{display:inline-block;height:52px;line-height:52px;padding:0 26px;border-radius:26px;font-size:16px;text-decoration:none}
.btn-red{background:linear-gradient(90deg,var(--red),var(--red-dark));color:var(--white)}
.btn-white{background:var(--white);color:var(--ink)}
.hero .btn{margin-top:28px}
.deco{position:absolute;width:560px;height:560px;border-radius:50%;top:826px;background:radial-gradient(circle,#f1e6de,#faf6f3)}
.deco-left{left:-320px}
.deco-right{right:-320px}
.section-title{font-family:"Poppins",sans-serif;font-weight:500;font-size:42px;text-align:center;position:absolute;left:0;width:1200px}
.lead{position:absolute;left:290px;width:620px;text-align:center;font-size:14px;line-height:26px;color:#555}
.cards{position:absolute;top:958px;left:77px;display:flex;gap:29px}
.card{width:240px;height:313px;background:var(--blue);color:var(--white);text-align:center;padding-top:32px}
.card.featured{background:linear-gradient(90deg,var(--red),var(--red-dark))}
.card-icon{width:68px;height:68px;margin:0 auto;border:2px solid var(--white);border-radius:50%}
.card h3{font-family:"Lato",sans-serif;font-weight:400;font-size:20px;margin-top:22px}
.card p{font-size:14px;line-height:26px;margin:12px 18px 0}
.card .btn{margin-top:20px;padding:0 26px}
.bio{position:absolute;left:235px;width:730px;text-align:center;font-size:14px;line-height:26px;color:var(--grey-light)}
.newsletter{position:absolute;top:1752px;left:77px;width:1046px;height:312px;background:linear-gradient(90deg,var(--blue),var(--blue-light));text-align:center;color:var(--white)}
.newsletter h2{font-family:"Poppins",sans-serif;font-weight:600;font-size:35px;line-height:47px;margin-top:50px}
.form{display:flex;gap:21px;justify-content:center;margin-top:30px}
.field{width:260px;height:62px;border-radius:31px;background:var(--white);color:#666;font-size:15px;text-align:left;padding-left:13px;line-height:62px}
.submit{width:188px;height:62px;border-radius:31px;background:linear-gradient(90deg,var(--red),var(--red-dark));font-size:18px;line-height:62px}
.contact{position:absolute;top:2064px;left:77px;width:1046px;height:198px;background:var(--panel);display:flex;padding:58px 0 0 34px;font-size:14px;color:#555;line-height:26px}
.contact-intro{width:268px}
.contact-intro strong{display:block;font-family:"Poppins",sans-serif;font-weight:500;font-size:15px;color:var(--ink);margin-bottom:6px}
.contact-item{display:flex;gap:18px;width:268px}
.contact-icon{flex:none;width:52px;height:52px;background:var(--white);box-shadow:0 2px 6px rgba(0,0,0,.08);display:flex;align-items:center;justify-content:center}
.site-footer{position:absolute;top:2310px;left:77px;width:1046px;display:flex;align-items:center}
.copy{margin-left:100px;font-size:12px;color:var(--grey)}
.copy b{color:var(--ink)}
.social{margin-left:auto;display:flex;gap:11px}
.social span{width:52px;height:52px;border:1px solid #ddd}
.social span.on{background:var(--blue);border-color:var(--blue)}
</style>
</head>
<body>
<header class="site-header">
  <div class="brand"><span class="brand-dot"></span><span class="brand-name">BELVAN</span></div>
  <nav class="nav">
    <span class="active">Home</span><span>Treatments</span><span>New Patient Paperwork</span><span>Stretching</span><span>Photo Gallery</span><span>Contact</span>
    <svg width="22" height="22" viewBox="0 0 22 22" fill="none" stroke="#0e9acd" stroke-width="2"><circle cx="9" cy="9" r="7"/><path d="M14 14l6 6"/></svg>
  </nav>
</header>

<section class="hero" role="img" aria-label="Athlete stretching his hamstring on a running track in front of city buildings">
  <div class="hero-text">
    <h1>BELVAN CHIROPRACTIC AND SPORTS THERAPY</h1>
    <p>Lorem ipsum dolor sit amet, consectetur adipiscing elit, sed do eiusmod tempor incididunt ut labore et dolore magna aliqua.</p>
    <a class="btn btn-red" href="#">Read More</a>
  </div>
</section>

<div class="deco deco-left" role="img" aria-label="Faded photo of a therapy massage"></div>
<div class="deco deco-right" role="img" aria-label="Faded photo of a therapist treating an arm"></div>

<h2 class="section-title" style="top:795px">Treatments Offered</h2>
<p class="lead" style="top:870px">Lorem ipsum dolor sit amet, consectetur adipiscing elit, sed do eiusmod tempor incididunt ut laboris nisi ut aliquip ex ea commodo consequat.</p>

<div class="cards">
  <div class="card"><div class="card-icon" role="img" aria-label="Stretching figure icon"></div><h3>the Belvan Protocol</h3><p>Lorem ipsum dolor consectetur adipiscing elit, sed aliqua.</p><a class="btn btn-white" href="#">Read More</a></div>
  <div class="card"><div class="card-icon" role="img" aria-label="Yoga figure icon"></div><h3>Myofascial Release</h3><p>Lorem ipsum dolor consectetur adipiscing elit, sed aliqua.</p><a class="btn btn-white" href="#">Read More</a></div>
  <div class="card featured"><div class="card-icon" role="img" aria-label="Lunging figure icon"></div><h3>Active Release Therapy</h3><p>Lorem ipsum dolor consectetur adipiscing elit, sed aliqua.</p><a class="btn btn-white" href="#">Read More</a></div>
  <div class="card"><div class="card-icon" role="img" aria-label="Side stretch figure icon"></div><h3>Triggre Point Therapy</h3><p>Lorem ipsum dolor consectetur adipiscing elit, sed aliqua.</p><a class="btn btn-white" href="#">Read More</a></div>
</div>

<h2 class="section-title" style="top:1325px">Dr. Wade Belvan</h2>
<p class="bio" style="top:1404px;left:300px;width:600px">Dr. Wade Belvan is the owner and clinic director for Belvan Chiropractic and Sports Therapy. He is a native Texan, growing up in the Dallas area and attended the Northfield State University on a basketball scholarship.</p>
<p class="bio" style="top:1498px">Upon finishing his academic and basketball career at NSU, Dr. Belvan traveled and worked throughout Europe for 3 years before discovering beach volleyball and relocating to Miami Beach, FL. It was while competing on the East Coast pro-beach volleyball circuit that he experienced the awesome power of chiropractic and physical medicine.</p>
<a class="btn btn-red" href="#" style="position:absolute;top:1635px;left:532px;width:136px;text-align:center;padding:0">Read More</a>

<section class="newsletter">
  <h2>Stay Tuned for Our Updates. Sign Up<br>for the Newsletter!</h2>
  <div class="form">
    <div class="field">Enter Your Name :</div>
    <div class="field">Enter Your Email :</div>
    <div class="submit">Submit Now</div>
  </div>
</section>

<section class="contact">
  <div class="contact-intro"><strong>Get Your Body Relax Today!</strong>We have our own Therapy department to ensure your comfort</div>
  <div class="contact-item"><span class="contact-icon"><svg width="18" height="22" viewBox="0 0 18 22" fill="none" stroke="#d7141f" stroke-width="2"><path d="M9 21s7-7 7-12A7 7 0 0 0 2 9c0 5 7 12 7 12z"/><circle cx="9" cy="9" r="2.5"/></svg></span><span>418 Meridian Ave<br>Cedar Falls, TX 75210</span></div>
  <div class="contact-item"><span class="contact-icon"><svg width="20" height="20" viewBox="0 0 20 20"><path fill="#d7141f" d="M4 1l4 4-2 3c1 3 3 5 6 6l3-2 4 4-3 3C8 19 1 12 1 4z"/></svg></span><span style="padding-top:12px">info@belvanspinefit.com</span></div>
  <div class="contact-item"><span class="contact-icon"><svg width="22" height="16" viewBox="0 0 22 16"><rect width="22" height="16" fill="#d7141f"/><path d="M1 1l10 8 10-8M1 15l7-6M21 15l-7-6" stroke="#fff" stroke-width="1.5" fill="none"/></svg></span><span>555.214.3380 (P)<br>555.214.3381 (F)</span></div>
</section>

<footer class="site-footer">
  <div class="brand"><span class="brand-dot"></span><span class="brand-name">BELVAN</span></div>
  <p class="copy">Copyright © <b>BELVAN</b> - 2019 . All Right Reserved</p>
  <div class="social">
    <span class="on" role="img" aria-label="Social profile"></span>
    <span role="img" aria-label="Social profile"></span>
    <span role="img" aria-label="Social profile"></span>
    <span role="img" aria-label="Social profile"></span>
  </div>
</footer>
</body>
</html>
```